New CORPORATE WEBSITE DESIGN (Graphic layout for a WEBSITE TEMPLATE required - Photoshop files)

Hi – I need a draft created for a new corporate website for our company.
I need a graphic design concept which can be applied to a whole website layout -
I have a separate web development team who will implement the design onto Wordpress.
We are an Asian Buying Office based in Hong Kong and Shenzhen which facilitates relationships between factories in China and customers (retailers/etailers) all over the world.
We are a “boutique” agency, which offers highly customized services – we are highly consultative in our approach and tailor services to suit the needs of our customers with customized solutions. Our services are transparent partnership- and-integrity-based, and aimed to support at a certain size of company in growth mode.
We have dedicated teams of staff focused entirely on a customer’s business and we work TOGETHER with customers to solve their product design, patent, product engineering, goods production, quality control and supply chain challenges operating in 24/7 through our proprietary web-based supply chain platform called Cargoloom.
I have a PowerPoint which can be used to drive:
1) creative direction (colour palette etc) and to provide basic content for each “screen.” I would like to see design options based on the PowerPoint which offer creative ways to create a new look and feel for us for a corporate website which will not be social media enabled or ecommerce enabled. We do not put ANY customer brand names direct or references on our website – relationships are private. The home page of the website should say in the design style – “product design and branded global consumer goods” as well as “professional engineering and quality control proficiency”.
The website should be clean and functional – have the “usability” of the Pebble website but the “Meridian 300” look & feel of the Tan & Voss website (http://www.tanvoss-example.com/eng/global/home.php) – Tan & Voss is a benchmark for us. Tan & Voss is the largest company in our industry doing what we do.
I do not want to COPY this example - I am offering it as a benchmark for a CLEAN, vibrant, professional site which sends a good brand and services message. The target market is a global B to B market – SMEs who are well funded and growing, brands with growth potential, or large, established brands who are looking to a) build a supply chain partner to help them grow b) increase their revenues by managing their costs c) reduce their risk through an experience buyer’s agent such as ourselves – a partner with integrity who they can trust. The web site design must say “global consumer brands” WITHOUT DIRECTLY ALLUDING TO THE LOGOS AND/OR BRAND NAMES WE WORK WITH , " full service agency – managing the process from product design and engineering, quality control and risk management to product manufacturing and shipping logistics" and “accountability/integrity/transparency within the partnership.” Designer to choose colors to be used in the design - I have also attached my logo file to allow you to select a color palette which will be complementary.
PLEASE FEEL FREE TO ASK ANY QUESTIONS - I AM HAPPY TO PROVIDE MORE DETAILS.

```html
<!DOCTYPE html>
<html lang="en">
<head>
<meta charset="utf-8">
<title>Orvane Trading Limited – Home</title>
<link href="https://fonts.googleapis.com/css2?family=Raleway:wght@400;500&family=Open+Sans:wght@400&display=swap" rel="stylesheet">
<style>
:root{
  --navy:#0d3b78;
  --text-grey:#555a60;
  --footer-bg:#e9e9ea;
  --footer-text:#6a6d72;
  --icon-grey:#6f7277;
  --white:#ffffff;
}
*{margin:0;padding:0;box-sizing:border-box}
html,body{width:1200px;height:1127px;overflow:hidden;background:var(--white)}
body{position:relative;font-family:"Raleway",sans-serif;color:var(--text-grey)}

.site-header{position:absolute;left:0;top:0;width:1200px;height:117px;background:#f8f8f9}
.brand{position:absolute;left:75px;top:16px;display:flex;align-items:center;gap:10px}
.brand-mark{width:72px;height:72px;border-radius:50%;background:var(--navy)}
.brand-name{font-weight:500;font-size:22px;line-height:1.05;color:var(--navy)}
.brand-tagline{position:absolute;left:236px;top:76px;font-size:11px;letter-spacing:.5px;color:#666;white-space:nowrap}

.search{position:absolute;left:890px;top:15px;width:238px;height:30px;border:1px solid #cfd1d4;background:var(--white);display:flex}
.search-field{flex:1;font-family:"Open Sans",sans-serif;font-size:13px;color:#555;padding:6px}
.search-button{width:28px;height:28px;background:#8a8c90;display:flex;align-items:center;justify-content:center}

.main-nav a{position:absolute;top:70px;transform:translateX(-50%);font-size:12.5px;color:var(--text-grey);text-decoration:none;white-space:nowrap;padding-bottom:8px}
.main-nav a.is-active{color:var(--navy);font-weight:500;border-bottom:3px solid var(--navy);padding:0 5px 8px}

.hero{position:absolute;left:0;top:117px;width:1200px;height:568px;
  background:
   linear-gradient(180deg,rgba(245,240,235,.25) 0%,rgba(60,55,55,.15) 35%,rgba(40,38,40,.45) 100%),
   linear-gradient(100deg,#9b6a52 0%,#b23a4c 14%,#7a2f3a 26%,#8d8578 38%,#5e5a55 48%,#1f6e66 60%,#a82e36 74%,#6a3a7a 82%,#c9b58a 100%)}
.hero-arrow{position:absolute;top:386px}
.hero-caption{position:absolute;left:140px;top:482px;width:680px;color:var(--white)}
.hero-title{font-size:33px;font-weight:400;margin-bottom:14px;line-height:1.15}
.hero-text{font-size:18px;line-height:22px}

.feature{position:absolute;top:693px;height:282px;display:flex;justify-content:center}
.feature h2{margin-top:34px;font-size:19px;font-weight:400;color:var(--white)}
.feature--sourcing{left:0;width:390px;background:linear-gradient(160deg,#6c93c4 0%,#4a77b2 55%,#1f3f78 100%)}
.feature--risk{left:399px;width:407px;background:radial-gradient(circle at 50% 62%,#234f8d 0%,#0d3b78 60%)}
.feature--brand{left:814px;width:386px;background:linear-gradient(170deg,#7f9fc6 0%,#6a8ab2 60%,#9c8a8a 100%)}

.site-footer{position:absolute;left:0;top:984px;width:1200px;height:143px;background:var(--footer-bg)}
.footer-nav a{position:absolute;top:25px;transform:translateX(-50%);font-size:13px;color:var(--footer-text);text-decoration:none;white-space:nowrap}
.copyright{position:absolute;top:57px;left:0;width:1200px;text-align:center;font-size:12px;color:#8b8d91}
.size-flag{position:absolute;right:20px;top:70px;font-size:10px;color:#555}
.social{position:absolute;top:91px;left:528px;display:flex;gap:6px}
.social span{width:34px;height:34px;border-radius:50%;background:var(--icon-grey)}
</style>
</head>
<body>
<header class="site-header">
  <div class="brand">
    <div class="brand-mark"></div>
    <div class="brand-name">Orvane<br>Trading Limited</div>
  </div>
  <div class="brand-tagline">Asian Sourcing Expertise</div>

  <div class="search">
    <div class="search-field">Search</div>
    <div class="search-button">
      <svg width="18" height="18" viewBox="0 0 18 18"><circle cx="7" cy="7" r="5" fill="none" stroke="#fff" stroke-width="2.2"/><line x1="11" y1="11" x2="16" y2="16" stroke="#fff" stroke-width="2.6" stroke-linecap="round"/></svg>
    </div>
  </div>

  <nav class="main-nav">
    <a class="is-active" style="left:502px">HOME</a>
    <a style="left:583px">ABOUT US</a>
    <a style="left:686px">WHO WE ARE</a>
    <a style="left:787px">SERVICES</a>
    <a style="left:885px">HIGHLIGHTS</a>
    <a style="left:985px">LOGISTICS</a>
    <a style="left:1087px">CONTACT US</a>
  </nav>
</header>

<section class="hero" role="img" aria-label="Photo of colourful clutch handbags on glass display shelves"></section>
<svg class="hero-arrow" style="left:72px" width="32" height="32" viewBox="0 0 32 32"><circle cx="16" cy="16" r="14" fill="none" stroke="#fff" stroke-width="2"/><path d="M9 16h14M9 16l6-6M9 16l6 6" fill="none" stroke="#fff" stroke-width="3" stroke-linecap="round"/></svg>
<svg class="hero-arrow" style="left:1094px" width="32" height="32" viewBox="0 0 32 32"><circle cx="16" cy="16" r="14" fill="none" stroke="#fff" stroke-width="2"/><path d="M23 16H9M23 16l-6-6M23 16l-6 6" fill="none" stroke="#fff" stroke-width="3" stroke-linecap="round"/></svg>
<div class="hero-caption">
  <h1 class="hero-title">Product design and branded global consumer goods</h1>
  <p class="hero-text">Professional engineering and quality control proficiency, from design to shipping logistics.</p>
</div>

<section class="feature feature--sourcing" role="img" aria-label="Two hands joining gears, tinted blue"><h2>Asia Sourcing Partnerships</h2></section>
<section class="feature feature--risk" role="img" aria-label="Illustration of figures around a hook, tinted navy"><h2>Supply Chain Risk Management</h2></section>
<section class="feature feature--brand" role="img" aria-label="Row of hands giving thumbs up, tinted blue"><h2>Global Brand Equity Enhancement</h2></section>

<footer class="site-footer">
  <nav class="footer-nav">
    <a style="left:350px">Home</a>
    <a style="left:419px">About Us</a>
    <a style="left:506px">Who we are</a>
    <a style="left:592px">Services</a>
    <a style="left:671px">Highlights</a>
    <a style="left:751px">Logistics</a>
    <a style="left:835px">Contact Us</a>
  </nav>
  <p class="copyright">All Rights Reserved. Copyrights @ 2014</p>
  <span class="size-flag">XS</span>
  <div class="social" aria-label="Social links">
    <span></span><span></span><span></span><span></span>
  </div>
</footer>
</body>
</html>
```